Hemp (cannabis) CBD Oil 3-page Blog website

The objective is 1) to look like professional/serious company, 2) to get investors excited about our Hemp business, 3) to get investor email and phone numbers and build a sense community. Potential investors should become excited that this is their “window of opportunity,” because VeltoriKa is made up of extraordinary people who all have made successful business before, that the location in Uruguay is a huge benefit, that we will become the biggest and best CBD-oil manufacturer in Latin America, and that we focus on all-legal medicinal CBD oil extracted from hemp.

Target Market(s)

Potential investors looking to invest between $30,000-$1,000,000 USD into a HEMP startup business, based in Uruguay, South America.

Industry/Entity Type

Business

Number of Pages Required

3 page

Font styles to use
Sans Serif

Requirements
Must have
• Three pages: Home, Members Only, News (blog).
• FOR MORE DETAIL SEE ATTACHED WORD REQUIREMENTS DOCUMENT.
Nice to have
• Uruguay colors: sky blue, golden sun. Medicinal. Legal. Mainstream. Hemp. Professional people. Opportunity/Money/Investor. Uruguay. Latin America. 1st to Market.
Should not have
• Marijuana (HEMP yes, marijuana NO), anything that looks illegal.

```html
<!DOCTYPE html>
<html lang="en">
<head>
<meta charset="utf-8">
<title>VeltoriKa – Organic Hemp Oil</title>
<link rel="stylesheet" href="https://fonts.googleapis.com/css2?family=Lato:wght@300;400;700;900&family=Merriweather:wght@700&display=swap">
<style>
:root{
  --blue:#1f5aa6;
  --blue-dark:#173f7a;
  --green:#1bb07a;
  --lime:#7ab32e;
  --teal:#5cc5cf;
  --grey:#e5e6e6;
  --text:#4a4a4a;
  --muted:#777;
  --line:#d9d9d9;
}
*{box-sizing:border-box;margin:0;padding:0}
html,body{width:1200px;height:3279px;overflow:hidden}
body{position:relative;font-family:"Lato",sans-serif;color:var(--text);background:#fff}
.abs{position:absolute}
section,header,footer{position:absolute;left:0;width:1200px}

/* header + hero */
.hero{top:0;height:656px;background:linear-gradient(180deg,#6fa6dc 0%,#b9d6ef 30%,#7aa65a 55%,#3f6d2a 100%)}
.masthead{top:0;left:0;width:1200px;height:112px;background:rgba(255,255,255,.82)}
.topbar{top:0;left:754px;height:33px;width:318px;display:flex;font-size:15px;font-weight:700;color:#fff}
.topbar-phone{background:var(--blue-dark);flex:1;height:33px;display:flex;align-items:center;justify-content:center;gap:8px;border-radius:0 0 0 14px}
.topbar-members{background:var(--green);flex:1;height:33px;display:flex;align-items:center;justify-content:center;gap:8px}
.brand{left:98px;top:46px;display:flex;align-items:center;gap:10px;font-size:34px;font-weight:700;color:var(--blue)}
.brand i{width:16px;height:16px;border-radius:50%;background:var(--green);display:block}
.nav{top:66px;left:0;width:1200px;font-size:16px;font-weight:700;color:#1d2f4a}
.nav a{position:absolute;color:inherit;text-decoration:none}
.nav a.active::after{content:"";position:absolute;left:0;right:0;bottom:-8px;height:3px;background:var(--blue)}
.hero-circle{left:721px;top:213px;width:360px;height:360px;border-radius:50%;background:rgba(255,255,255,.92);box-shadow:0 0 0 14px rgba(255,255,255,.35);text-align:center}
.hero-circle h1{margin-top:110px;font-weight:300;font-size:29px;line-height:42px;color:var(--blue)}
.btn-shop{display:inline-block;margin-top:22px;background:var(--green);color:#fff;font-size:19px;font-weight:700;padding:8px 30px;border-radius:22px;letter-spacing:.5px}

.band{top:656px;height:81px;background:var(--green);color:#fff;font-size:34px;font-weight:700;display:flex;align-items:center;justify-content:center}

.title{width:1200px;text-align:center;font-weight:700;font-size:36px;color:var(--blue)}
.title span{color:var(--lime)}
.divider{height:1px;background:var(--line)}
.divider::after{content:"";position:absolute;left:50%;top:-5px;width:10px;height:10px;margin-left:-5px;border-radius:50%;background:#c8c8c8}

/* news */
.news-photo{width:234px;height:258px}
.news-card{width:250px;height:227px;background:#fff;border-radius:8px;box-shadow:0 2px 8px rgba(0,0,0,.18);padding:30px 16px 0 18px}
.news-card h3{font-size:15px;line-height:22px;color:var(--blue);font-weight:700}
.news-card p{font-size:12.5px;line-height:19px;color:var(--muted);margin-top:10px}
.news-card .more{display:block;margin-top:10px;font-size:12px;font-weight:700;color:var(--blue)}
.date{width:52px;text-align:center;font-weight:700}
.date .d{background:#fff;color:#333;font-size:22px;height:34px;line-height:34px}
.date .m{background:var(--green);color:#fff;font-size:15px;height:26px;line-height:26px}
.dots span{position:absolute;top:0;height:4px;width:38px}

/* about */
.about-lead{left:120px;width:960px;text-align:center;color:var(--green);font-weight:700;font-size:16.5px;line-height:33px}
.about-body{left:120px;width:950px;text-align:center;font-size:14px;line-height:24px;color:#555}
.pill{display:flex;align-items:center;border-radius:20px;background:#dcdcdc;color:var(--blue);font-weight:700;font-size:14px;height:36px;padding-left:22px}
.pill b{margin-left:auto;width:36px;height:36px;border-radius:50%;background:var(--blue);color:#fff;display:flex;align-items:center;justify-content:center;font-size:16px}
.bottle{left:1090px;top:640px;width:110px;height:278px;background:linear-gradient(180deg,rgba(230,190,120,.15),#d9a25b 60%,#b97c3a);border-radius:36px 0 0 0}

/* cbd */
.cbd{top:1655px;height:417px;background:var(--teal)}
.cbd-circle{left:433px;top:46px;width:314px;height:314px;border-radius:50%;background:#fff;box-shadow:0 0 0 12px rgba(255,255,255,.45);text-align:center}
.cbd-circle h2{margin-top:56px;font-size:36px;font-weight:900;color:var(--blue)}
.cbd-circle p{margin:12px auto 0;width:240px;font-size:14px;line-height:24px;color:#333}
.cbd-label{font-size:16px;line-height:20px;color:#1d2f4a}
.cbd-label.left{text-align:right;width:130px}

/* members area */
.members-area{top:2072px;height:241px}
.members-area h2{font-size:29px;font-weight:700;color:var(--blue)}
.members-area h2 span{color:var(--lime)}
.members-area p{font-size:13px;color:#555}
.field{height:38px;border:1px solid #b9c4d4;border-radius:2px;background:#fff;font-size:12px;color:#777;padding-left:10px;display:flex;align-items:center}

/* team */
.team{top:2313px;height:343px;background:var(--grey)}
.avatar{width:152px;height:152px;border-radius:50%;border:5px solid #fff;box-shadow:0 2px 6px rgba(0,0,0,.2)}
.member-name{width:170px;text-align:center;font-family:"Merriweather",serif;font-size:13px;color:#222}

/* contact */
.contact{top:2656px;height:280px}
.contact h2{font-weight:300;font-size:38px;line-height:46px;color:var(--green)}
.contact .intro{font-size:13px;line-height:19px;color:#555}
.btn-submit{display:flex;align-items:center;height:36px;border-radius:20px;background:var(--green);color:#fff;font-size:20px;font-weight:700;padding-left:20px}
.btn-submit b{margin-left:auto;width:36px;height:36px;border-radius:50%;background:var(--blue);display:flex;align-items:center;justify-content:center;font-size:15px}

/* footer */
.footer{top:2936px;height:299px;background:linear-gradient(180deg,#2a2f36,#14171b);color:#fff}
.footer h3{font-size:21px;font-weight:400}
.footer .link{font-size:14px;display:flex;align-items:center;gap:16px}
.footer .link::before{content:"";width:14px;height:2px;background:#9aa0a6}
.map{left:494px;top:37px;width:212px;height:223px;background:#fff;padding:10px}
.map div{width:100%;height:100%;background:linear-gradient(160deg,#f3c64f,#e87c4a 45%,#6fb4d9);opacity:.85}
.copy{top:3235px;left:0;width:1200px;height:44px;background:var(--green);color:#fff;font-size:14px;display:flex;align-items:center;justify-content:center}
</style>
</head>
<body>

<section class="hero" role="img" aria-label="Photograph of a hemp field under a blue sky"></section>
<header>
  <div class="abs masthead"></div>
  <div class="abs topbar">
    <div class="topbar-phone">
      <svg width="16" height="16" viewBox="0 0 16 16"><circle cx="8" cy="8" r="7" fill="none" stroke="#fff" stroke-width="1.5"/><path d="M5 4.5l2 1.5-1 1.5 2 2 1.5-1 1.5 2-1 1C7 11.5 4.5 9 4 6z" fill="#fff"/></svg>
      123 456 7890
    </div>
    <div class="topbar-members">
      <svg width="16" height="16" viewBox="0 0 16 16"><circle cx="8" cy="8" r="7" fill="none" stroke="#fff" stroke-width="1.5"/><circle cx="8" cy="6.5" r="2.2" fill="#fff"/><path d="M4.5 12c.8-2 2-2.8 3.5-2.8S10.7 10 11.5 12z" fill="#fff"/></svg>
      Members Only
    </div>
  </div>
  <div class="abs brand"><i></i>VeltoriKa</div>
  <nav class="abs nav">
    <a class="active" style="left:564px">Home</a>
    <a style="left:654px">About Us</a>
    <a style="left:767px">Our Team</a>
    <a style="left:886px">News</a>
    <a style="left:973px">Contact Us</a>
  </nav>
  <div class="abs hero-circle">
    <h1>Our Organic Hemp<br>Oil Solutions<br>Changes Lives</h1>
    <span class="btn-shop">SHOP NOW</span>
  </div>
</header>

<section class="band">Become A Member for Exclusive Insider Information</section>

<section style="top:737px;height:918px">
  <h2 class="abs title" style="top:30px">Latest <span>News</span></h2>
  <div class="abs divider" style="left:245px;width:710px;top:100px"></div>

  <div class="abs news-photo" style="left:98px;top:146px;background:linear-gradient(160deg,#dfe7ee,#8fb07a 50%,#3e6a2c)" role="img" aria-label="Photo of a greenhouse with hemp plants"></div>
  <div class="abs news-card" style="left:332px;top:166px">
    <h3>Duis autem vel eum iriure do in hendrerit in vulputate.</h3>
    <p>Duis auti vel eum iriure dolor in ik hendr vulputatel velit es molestie coni quat, vel illum dol dignissim qui blandit praesen lup delenitnil lanre facilisi.</p>
    <span class="more">Read More »</span>
  </div>
  <div class="abs date" style="left:280px;top:171px"><div class="d">06</div><div class="m">Oct</div></div>

  <div class="abs news-photo" style="left:623px;top:146px;width:230px;background:linear-gradient(170deg,#5f98d2,#a9c9e8 30%,#6b9a45 55%,#355f22)" role="img" aria-label="Photo of a grower inspecting hemp plants in a field"></div>
  <div class="abs news-card" style="left:853px;top:166px">
    <h3>Duis autem vel eum iriure do in hendrerit in vulputate.</h3>
    <p>Duis auti vel eum iriure dolor in ik hendr vulputatel velit es molestie coni quat, vel illum dol dignissim qui blandit praesen lup delenitnil lanre facilisi.</p>
    <span class="more">Read More »</span>
  </div>
  <div class="abs date" style="left:801px;top:171px"><div class="d">06</div><div class="m">Oct</div></div>

  <div class="abs dots" style="left:531px;top:450px;width:140px;height:4px">
    <span style="left:0;background:var(--lime)"></span>
    <span style="left:46px;background:var(--lime)"></span>
    <span style="left:92px;background:var(--blue)"></span>
  </div>

  <h2 class="abs title" style="top:496px">About <span>VeltoriKa</span></h2>
  <div class="abs divider" style="left:245px;width:710px;top:566px"></div>
  <p class="abs about-lead" style="top:601px">VeltoriKa Is A Manufacturing Startup Company In Uruguay, South America. It Will Grow A Specially Engineered Strain Of High CBD Hemp, Extract And Refine The Valuable Plant Oils, And Package The Oils Into Therapeutic Products.</p>
  <p class="abs about-body" style="top:694px">The products will be sold into countries where new markets exist due to deregulation of cannabis (hemp and marijuana), and will target specific diseases known to respond positively to CBD. In time the CBD oil will be infused into consumer products for mainstream consumption. Uruguay was chosen because its federal law enables a 3x more efficient CBD production than in the US, Canada or Europe. Additionally, VeltoriKa processing will be in the Free Trade Zone (FTZ) to eliminate many taxes and greatly reduce costs. Finally, Uruguayan law ensures our CBD production and export is 100% legal. Thus, VeltoriKa aims to be the most profitable, &amp; safest, CBD manufacturing company in the world.</p>
  <div class="abs pill" style="left:533px;top:839px;width:130px">Read More <b>»</b></div>
  <div class="abs bottle" role="img" aria-label="Photo of a CBD oil bottle with a dropper"></div>
</section>

<section class="cbd">
  <svg class="abs" style="left:0;top:0" width="1200" height="417" fill="none" stroke="#fff" stroke-width="1.5">
    <path d="M319 83H380L440 140"/><path d="M319 210H433"/><path d="M319 334H380L440 280"/>
    <path d="M863 83H800L740 140"/><path d="M863 210H747"/><path d="M863 334H800L740 280"/>
    <g fill="var(--teal)" stroke="#1d2f4a"><circle cx="319" cy="83" r="4"/><circle cx="319" cy="210" r="4"/><circle cx="319" cy="334" r="4"/><circle cx="863" cy="83" r="4"/><circle cx="863" cy="210" r="4"/><circle cx="863" cy="334" r="4"/></g>
    <g stroke="var(--blue)" stroke-width="2.5">
      <circle cx="262" cy="86" r="10"/><circle cx="280" cy="74" r="6"/>
      <circle cx="272" cy="208" r="14"/><path d="M258 208h28M272 194v28"/><path d="M282 218l10 10"/>
      <rect x="258" y="322" width="30" height="22" rx="3"/><path d="M267 322v-5h12v5M273 328v10M268 333h10"/>
      <path d="M885 92c0-14 10-22 20-24-2 10-8 18-20 24zM885 92c4-10 12-14 20-14"/>
      <path d="M898 200l-8 26M898 200l8 26M892 214h12M898 196v-6"/>
      <path d="M884 350V336M893 350V326M902 350V316M911 350V330M880 350h36"/>
    </g>
  </svg>
  <div class="abs cbd-label left" style="left:104px;top:63px">Genetic<br>Engineering</div>
  <div class="abs cbd-label left" style="left:104px;top:190px">New<br>Markets</div>
  <div class="abs cbd-label left" style="left:104px;top:314px">Therapeutic<br>Products</div>
  <div class="abs cbd-label" style="left:925px;top:63px">Hemp<br>Cultivation</div>
  <div class="abs cbd-label" style="left:925px;top:200px">Extraction</div>
  <div class="abs cbd-label" style="left:925px;top:314px">Oil<br>Refinement</div>
  <div class="abs cbd-circle">
    <h2>CBD</h2>
    <p>Our Hemp Was Engineered To Maximize Therapeutic CBD, Under Uruguayan Laws We Refine The Oil At 2x Higher Profitability Than Anywhere Else In The World</p>
  </div>
</section>

<section class="members-area">
  <h2 class="abs" style="left:103px;top:39px">Members <span>Only</span></h2>
  <div class="abs divider" style="left:98px;width:470px;top:90px"></div>
  <p class="abs" style="left:103px;top:114px">Guest Area. Please Enter the password below</p>
  <div class="abs field" style="left:98px;top:156px;width:215px">Enter Password</div>
  <div class="abs pill" style="left:332px;top:157px;width:100px">GO <b>»</b></div>

  <h2 class="abs" style="left:605px;top:39px">Invited people to <span>Get the Password</span></h2>
  <div class="abs divider" style="left:605px;width:500px;top:90px"></div>
  <p class="abs" style="left:609px;top:114px">Lorem ut wisi enim ad minim veniam, quis nostrm ci tation.</p>
  <div class="abs field" style="left:605px;top:156px;width:200px">Email Address</div>
  <div class="abs pill" style="left:824px;top:157px;width:131px">Submit <b>»</b></div>
</section>

<section class="team">
  <h2 class="abs title" style="top:40px">Our <span>Team</span></h2>
  <div class="abs" style="left:520px;top:96px;width:160px;height:3px;background:var(--blue)"></div>
  <div class="abs avatar" style="left:101px;top:125px;background:linear-gradient(160deg,#c9b59b,#7a6551)" role="img" aria-label="Portrait of a team member"></div>
  <div class="abs avatar" style="left:269px;top:125px;background:linear-gradient(160deg,#8aa07a,#3f5533)" role="img" aria-label="Portrait of a team member"></div>
  <div class="abs avatar" style="left:438px;top:125px;background:linear-gradient(160deg,#b8a694,#5c4a3e)" role="img" aria-label="Portrait of a team member"></div>
  <div class="abs avatar" style="left:608px;top:125px;background:linear-gradient(160deg,#7fa36c,#2f4f25)" role="img" aria-label="Portrait of a team member"></div>
  <div class="abs avatar" style="left:777px;top:125px;background:linear-gradient(160deg,#8c8f96,#2a2c31)" role="img" aria-label="Portrait of a team member"></div>
  <div class="abs avatar" style="left:947px;top:125px;background:linear-gradient(160deg,#c1b8b0,#5d5650)" role="img" aria-label="Portrait of a team member"></div>
  <div class="abs member-name" style="left:92px;top:293px">Lorem ipsum do</div>
  <div class="abs member-name" style="left:260px;top:293px">Lorem ipsum do</div>
  <div class="abs member-name" style="left:429px;top:293px">Lorem ipsum do</div>
  <div class="abs member-name" style="left:599px;top:293px">Lorem ipsum do</div>
  <div class="abs member-name" style="left:768px;top:293px">Lorem ipsum do</div>
  <div class="abs member-name" style="left:938px;top:293px">Lorem ipsum do</div>
</section>

<section class="contact">
  <h2 class="abs" style="left:98px;top:56px">Quick Contact<br>With Us</h2>
  <p class="abs intro" style="left:98px;top:152px;width:300px">Duis autem vel eum iriure dolormi opl inmokl hendi rerit in vulpu tatemi velitm essemol no molestiel conseqb uat, velmi illum dolor eokf no atn nulla more facilisis... [+]</p>
  <p class="abs" style="left:459px;top:50px;font-size:13px;color:#333">Please fill up bellow form</p>
  <div class="abs field" style="left:459px;top:83px;width:308px;height:44px">Name</div>
  <div class="abs field" style="left:791px;top:83px;width:311px;height:44px">Email</div>
  <div class="abs field" style="left:459px;top:136px;width:308px;height:44px">Phone</div>
  <div class="abs field" style="left:791px;top:136px;width:311px;height:44px">Message</div>
  <div class="abs btn-submit" style="left:459px;top:196px;width:131px">Submit <b>»</b></div>
</section>

<footer class="footer">
  <h3 class="abs" style="left:98px;top:52px">Quick Links</h3>
  <div class="abs link" style="left:110px;top:120px">Home</div>
  <div class="abs link" style="left:110px;top:159px">Members Only</div>
  <div class="abs link" style="left:110px;top:200px">About Us</div>
  <div class="abs link" style="left:275px;top:120px">Our Team</div>
  <div class="abs link" style="left:275px;top:159px">Latest News</div>
  <div class="abs link" style="left:275px;top:200px">Contact Us</div>

  <div class="abs map" role="img" aria-label="Map of South America highlighting Uruguay"><div></div></div>

  <h3 class="abs" style="left:763px;top:52px">Contact Detail</h3>
  <svg class="abs" style="left:763px;top:106px" width="16" height="22" viewBox="0 0 16 22"><path d="M8 1a7 7 0 0 1 7 7c0 5-7 13-7 13S1 13 1 8a7 7 0 0 1 7-7z" fill="none" stroke="#3b8fe0" stroke-width="2"/><circle cx="8" cy="8" r="2.5" fill="#3b8fe0"/></svg>
  <div class="abs" style="left:790px;top:104px;font-size:21px">VeltoriKa</div>
  <div class="abs" style="left:790px;top:134px;font-size:14px;line-height:20px">123, Ut wisi enim ad minim veniam,<br>Mor nostrni tation -123 456</div>
  <svg class="abs" style="left:768px;top:186px" width="16" height="16" viewBox="0 0 16 16"><path d="M3 1l3 3-2 2c1 2 3 4 5 5l2-2 3 3-2 3C7 15 1 9 1 3z" fill="#3b8fe0"/></svg>
  <div class="abs" style="left:796px;top:186px;font-size:14px">123-456-7891</div>
  <svg class="abs" style="left:929px;top:186px" width="16" height="16" viewBox="0 0 16 16"><path d="M3 1l3 3-2 2c1 2 3 4 5 5l2-2 3 3-2 3C7 15 1 9 1 3z" fill="#3b8fe0"/></svg>
  <div class="abs" style="left:955px;top:186px;font-size:14px">123-456-7890</div>
  <svg class="abs" style="left:768px;top:229px" width="16" height="12" viewBox="0 0 16 12"><rect x="1" y="1" width="14" height="10" fill="none" stroke="#3b8fe0" stroke-width="1.5"/><path d="M1 1l7 6 7-6" fill="none" stroke="#3b8fe0" stroke-width="1.5"/></svg>
  <div class="abs" style="left:796px;top:226px;font-size:14px">mail@veltorika.com</div>
</footer>
<div class="abs copy">Copyright © 2017 VeltoriKa. All Rights Reserved.</div>

</body>
</html>
```